Hip surgeon needs a stationery design

I need a new stationery design for my private practice.
My practice is focused in hip arthroplasty (hip prosthesis).
I'd like to see designs most in blue or shades of blue.
I've uploaded my new logo to help with the task.
Also, I'm a member of some societies and I've uploaded their logos either, so I'd like to see them in some of the stationeries.
Itens list:
business card
letterhead A4
envelope
prescription block A5
one fold for A4 (please see the archive "pocket")
Personal data:
Dr. Renan L. Vasconti
CRM/PR 57316
site: www.clinicapelvora.com.br
email: dr.renan@clinicapelvora.com.br
Adress:
Rua Leopoldo Marques Vieira de Lima, 712
Campo Sereno - Curitiba/PR
41 30875316 I 30875317
Updates
I forgot to mention that my practice is focused primarily in hip arthroplasty (total hip prosthesis) and the target audience range from young adults to the elderly.
I also perform hip preserving surgeries (open and arthroscopic procedures) and pelvic and hip fracture surgery (trauma).
- Any "cleaner" fonts are welcome

```html
<!DOCTYPE html>
<html lang="pt-BR">
<head>
<meta charset="utf-8">
<title>Pasta A4 – Dr. Renan L. Vasconti</title>
<link href="https://fonts.googleapis.com/css2?family=Roboto:wght@300;400;500&display=swap" rel="stylesheet">
<style>
  :root {
    --stage: #ededed;
    --paper: #ffffff;
    --paper-inner: #f4f5f6;
    --blue-deep: #0b5fa5;
    --blue-bright: #0099d8;
    --blue-brand: #1a8fd0;
    --blue-soft: #42aee3;
    --text-light: #e6f3fb;
  }
  * { margin: 0; padding: 0; box-sizing: border-box; }
  html, body { width: 1200px; height: 1200px; overflow: hidden; }
  body {
    background: var(--stage);
    font-family: "Roboto", Arial, sans-serif;
    position: relative;
  }
  .spread {
    position: absolute;
    left: 260px;
    width: 680px;
    height: 480px;
    display: flex;
    box-shadow: 0 18px 40px rgba(0,0,0,0.12);
  }
  .spread--outside { top: 50px; }
  .spread--inside { top: 660px; }
  .panel { position: relative; width: 340px; height: 480px; overflow: hidden; }

  .back-cover {
    background: linear-gradient(90deg, var(--blue-deep), var(--blue-bright));
  }
  .contact {
    position: absolute;
    left: 22px;
    bottom: 22px;
    list-style: none;
    color: var(--text-light);
    font-size: 6.5px;
    line-height: 9px;
  }
  .contact li { display: flex; align-items: flex-start; gap: 6px; }
  .contact svg { width: 6px; height: 6px; margin-top: 1.5px; flex: none; }

  .front-cover { background: var(--paper); }
  .brand {
    position: absolute;
    left: 58px;
    top: 140px;
    display: flex;
    align-items: center;
    gap: 8px;
  }
  .brand-dot {
    width: 28px; height: 28px;
    border-radius: 50%;
    background: var(--blue-brand);
  }
  .brand-name {
    color: var(--blue-brand);
    font-weight: 500;
    font-size: 17px;
    line-height: 18px;
  }
  .brand-tagline {
    color: var(--blue-soft);
    font-weight: 400;
    font-size: 11px;
    line-height: 13px;
  }

  .inner-left { background: var(--paper); }
  .inner-right { background: var(--paper-inner); }
  .pocket { position: absolute; left: 0; bottom: 0; width: 340px; height: 220px; }
</style>
</head>
<body>

<section class="spread spread--outside" aria-label="Parte externa da pasta">
  <div class="panel back-cover">
    <ul class="contact">
      <li>
        <svg viewBox="0 0 10 10"><path d="M5 0a3.5 3.5 0 0 0-3.5 3.5C1.5 6 5 10 5 10s3.5-4 3.5-6.5A3.5 3.5 0 0 0 5 0z" fill="currentColor"/></svg>
        <span>Rua Leopoldo Marques Vieira de Lima,<br>712 Campo Sereno - Curitiba/PR</span>
      </li>
      <li>
        <svg viewBox="0 0 10 10"><path d="M2 0l2 2.5-1 1.5a6 6 0 0 0 3 3l1.5-1L10 8l-1.5 2C4 10 0 6 0 1.5z" fill="currentColor"/></svg>
        <span>41 30875316 I 30875317</span>
      </li>
      <li>
        <svg viewBox="0 0 10 10"><rect x="0" y="2" width="10" height="6.5" rx="1" fill="currentColor"/></svg>
        <span>dr.renan@clinicapelvora.com.br</span>
      </li>
      <li>
        <svg viewBox="0 0 10 10"><circle cx="5" cy="5" r="5" fill="currentColor"/></svg>
        <span>www.clinicapelvora.com.br</span>
      </li>
    </ul>
  </div>
  <div class="panel front-cover">
    <div class="brand">
      <span class="brand-dot"></span>
      <div>
        <div class="brand-name">Dr. Renan L. Vasconti</div>
        <div class="brand-tagline">Cirurgia do Quadril</div>
      </div>
    </div>
  </div>
</section>

<section class="spread spread--inside" aria-label="Parte interna da pasta com bolsos">
  <div class="panel inner-left">
    <svg class="pocket" viewBox="0 0 340 220" preserveAspectRatio="none">
      <defs>
        <linearGradient id="pocket-left" x1="0" x2="1" y1="0" y2="0">
          <stop offset="0" stop-color="#0b6fb0"/>
          <stop offset="1" stop-color="#0d6db5"/>
        </linearGradient>
      </defs>
      <path d="M0 56 L300 8 Q318 5 322 22 L340 220 L0 220 Z" fill="url(#pocket-left)"/>
      <path d="M4 60 L300 13" stroke="#9cc9e8" stroke-width="0.6" stroke-dasharray="2 2" fill="none"/>
    </svg>
  </div>
  <div class="panel inner-right">
    <svg class="pocket" viewBox="0 0 340 220" preserveAspectRatio="none">
      <defs>
        <linearGradient id="pocket-right" x1="0" x2="1" y1="0" y2="0">
          <stop offset="0" stop-color="#0b60a3"/>
          <stop offset="1" stop-color="#009cdc"/>
        </linearGradient>
      </defs>
      <path d="M18 220 L2 30 Q0 12 22 10 L340 0 L340 220 Z" fill="url(#pocket-right)"/>
      <path d="M24 15 L336 5" stroke="#9cd3ef" stroke-width="0.6" stroke-dasharray="2 2" fill="none"/>
    </svg>
  </div>
</section>

</body>
</html>
```